Brett Olsen Building Business Card Design

Hi,

I need a business card for my Building company.
I am a Builder and build homes for clients.
I am looking for a sophisticated logo that can be used on business cards, envelopes and letter heads.
I am trying to take my business to the next level and need a professional business card.

Colours: Please use white, black, dark grey and bright blue.

Thank you,

Carol and Brett.

Target Market(s)

1. Home and Building Companies 2. Potential customers

Industry/Entity Type

Business

Contact Information for Business Card

Brett Olsen Building PTY LTD

Brett Olsen

Director

A.B.N. 37 829 516 073

BUILDERS LICENCE No. 573019k

Mobile: 0412 907 381

Email: brettolsenbuilding@mailvane.com.au

Requirements
Must have
• The following is compulsory to have in the designs:

Brett Olsen Building PTY LTD (business name)

Brett Olsen (contact name)

Director (position)

A.B.N. 37 829 516 073

Builders Licence No. 573019k

Mobile: 0412 907 381

Nice to have
• Logo for business
Should not have
• Should not be cluttered.

I am looking for a clean, sophisticated and professional business card design.

```html
<!DOCTYPE html>
<html lang="en">
<head>
<meta charset="utf-8">
<title>Brett Olsen Building – Business Card</title>
<link rel="stylesheet" href="https://fonts.googleapis.com/css2?family=Tinos:wght@400;700&display=swap">
<style>
  :root {
    --sky-top: #95c8cc;
    --sky-mid: #7f9fce;
    --sky-low: #6966cf;
    --ink-white: #ffffff;
    --rule-grey: #d9d9de;
    --brand-red: #c3232b;
    --page: #ffffff;
  }
  html, body {
    margin: 0;
    padding: 0;
    width: 1200px;
    height: 733px;
    overflow: hidden;
    background: var(--page);
  }
  .card {
    position: relative;
    width: 1200px;
    height: 733px;
    border-radius: 20px;
    overflow: hidden;
    background: linear-gradient(180deg, var(--sky-top) 0%, var(--sky-mid) 38%, var(--sky-low) 72%, var(--sky-low) 100%);
    font-family: "Tinos", "Times New Roman", serif;
    color: var(--ink-white);
  }
  .swoosh {
    position: absolute;
    inset: 0;
    width: 1200px;
    height: 733px;
  }
  .holder-name {
    position: absolute;
    left: 43px;
    top: 236px;
    margin: 0;
    font-size: 57px;
    font-weight: 700;
    line-height: 1;
    letter-spacing: 0.5px;
  }
  .holder-rule {
    position: absolute;
    left: 41px;
    top: 297px;
    width: 352px;
    height: 4px;
    background: var(--rule-grey);
  }
  .holder-role {
    position: absolute;
    left: 45px;
    top: 309px;
    margin: 0;
    font-size: 25px;
    font-weight: 700;
    line-height: 1;
  }
  .details {
    position: absolute;
    left: 49px;
    top: 0;
    margin: 0;
    padding: 0;
    list-style: none;
    font-size: 27px;
    line-height: 1;
  }
  .details li {
    position: absolute;
    left: 0;
    white-space: nowrap;
  }
  .details .abn { top: 424px; }
  .details .licence { top: 495px; }
  .details .mobile { top: 567px; }
  .details .email { top: 640px; }
  .company-name {
    position: absolute;
    right: 49px;
    top: 375px;
    margin: 0;
    font-size: 35px;
    font-weight: 400;
    line-height: 1;
    color: var(--brand-red);
    white-space: nowrap;
  }
</style>
</head>
<body>
<main class="card">
  <svg class="swoosh" viewBox="0 0 1100 672" preserveAspectRatio="none" aria-hidden="true">
    <defs>
      <linearGradient id="swooshFade" x1="0" y1="0" x2="1" y2="1">
        <stop offset="0" stop-color="#ffffff" stop-opacity="0.12"/>
        <stop offset="0.45" stop-color="#ffffff" stop-opacity="0.45"/>
        <stop offset="1" stop-color="#ffffff" stop-opacity="0.9"/>
      </linearGradient>
    </defs>
    <path d="M42 296 C180 308 330 312 430 322 C640 342 790 470 858 672 L706 672 C690 540 660 440 560 392 C470 350 300 352 42 376 Z" fill="url(#swooshFade)"/>
  </svg>

  <h1 class="holder-name">Brett Olsen</h1>
  <div class="holder-rule"></div>
  <p class="holder-role">Director</p>

  <ul class="details">
    <li class="abn">A.B.N. 37 829 516 073</li>
    <li class="licence">Builders Licence No. 573019k</li>
    <li class="mobile">Mobile: 0412 907 381</li>
    <li class="email">Email: brettolsenbuilding@mailvane.com.au</li>
  </ul>

  <p class="company-name">Brett Olsen Building PTY LTD</p>
</main>
</body>
</html>
```